***Flyer*** TORNILEX AUTO TRANSPORT *** Flyer***

I need a flyer design that explain my auto transport business... the design must be eye catching and draws a persons attention at first site. We Tow Cars locally in the City of Houston for a flat rate of $75... We ask that the designer make the $75 standout so it will catch the attention of the reader. Much of the content writing can be gather from my website tornilexautotransport.com - the designer can use his own images to express his design work... I will attach the logo and some samples of some reason business and post cards designs. If you chose you can also add these images in your designs if it will help.

Size of flyer is 8"x11" front and back

Automotive

Requirements
Must have
• $75 or $75.00
• (281) 555-0137
• service@tornilexautotransport.com
• www.tornilexautotransport.com
Nice to have
• WE REALLY WANT TO EARN YOUR BUSINESS
• Note: Please look at my website for content writing to create your flyer.

```html
<!DOCTYPE html>
<html lang="en">
<head>
<meta charset="utf-8">
<title>Tornilex Auto Transport – Towing Flyer</title>
<link rel="stylesheet" href="https://fonts.googleapis.com/css2?family=Arimo:wght@400;700&display=swap">
<style>
  :root{
    --red:#ff0a0a;
    --red-deep:#e01010;
    --pink-bar:#f7a0a6;
    --white:#ffffff;
    --ink:#111111;
    --ink-soft:#2a2a2a;
    --brand-grey:#3a3a3a;
    --tyre-dark:#1b1b1d;
    --tyre-mid:#5a5b5e;
    --tyre-hub:#c9cacb;
  }
  *{margin:0;padding:0;box-sizing:border-box}
  html,body{width:873px;height:1200px;overflow:hidden;background:#fff}
  body{font-family:"Arimo",Arial,sans-serif}
  .flyer{position:relative;width:873px;height:1200px;overflow:hidden;
    background:linear-gradient(180deg,#dfe6ec 0%,#c9d2da 22%,#9aa3ad 45%,#6c7179 70%,#3b3d42 100%)}
  .backdrop-top{position:absolute;left:380px;top:0;width:493px;height:300px;
    background:linear-gradient(180deg,#eef2f5 0%,#b7c2cc 45%,#8e9aa5 75%,#9ca58e 100%)}
  .backdrop-left{position:absolute;left:0;top:460px;width:330px;height:660px;
    background:linear-gradient(160deg,#7f96b2 0%,#4c5a70 35%,#a6adb6 65%,#2a2c30 100%)}
  svg.shapes{position:absolute;left:0;top:0}
  .brand{position:absolute;left:30px;top:118px;width:340px;text-align:center;color:var(--brand-grey);font-weight:700}
  .brand .name{font-size:46px;letter-spacing:-1px;line-height:1}
  .brand .tag{font-size:22px;margin-top:8px;line-height:1}
  .offer{position:absolute;left:360px;width:560px;text-align:center;font-weight:700}
  .headline{top:402px;color:var(--white);font-size:53px;line-height:66px;letter-spacing:.5px}
  .price{top:598px;color:var(--red);font-size:70px;line-height:1}
  .price-label{top:684px;color:var(--ink);font-size:31px}
  .promise{color:var(--white);font-size:23px;line-height:1;text-shadow:0 1px 2px rgba(0,0,0,.45)}
  .promise .hot{color:var(--red);font-size:31px;text-shadow:none}
  .p1{top:773px;left:300px;width:580px}
  .p2{top:816px;left:300px;width:440px}
  .p3{top:862px;left:300px;width:560px}
  .p4{top:893px;left:300px;width:560px}
  .closer{top:968px;left:350px;width:520px;color:var(--ink-soft);font-size:31px;line-height:45px}
  .contact{position:absolute;left:0;display:flex;align-items:center;gap:14px;padding-left:10px;
    background:linear-gradient(90deg,var(--red-deep) 0%,var(--pink-bar) 70%,#ffd8db 100%);
    border-radius:0 8px 8px 0;font-weight:700;color:var(--ink)}
  .contact svg{flex:none}
  .c-phone{top:1042px;width:364px;height:38px;font-size:21px}
  .c-web{top:1100px;width:362px;height:36px;font-size:17px}
  .c-mail{top:1153px;width:418px;height:38px;font-size:17px}
</style>
</head>
<body>
<main class="flyer">
  <div class="backdrop-top" role="img" aria-label="Photo of car carrier trucks loaded with compact cars"></div>
  <div class="backdrop-left" role="img" aria-label="Photo of a tow truck carrier on the road"></div>

  <svg class="shapes" width="873" height="1200" viewBox="0 0 873 1200" aria-hidden="false">
    <defs>
      <radialGradient id="tyre-large" cx="0.45" cy="0.45" r="0.6">
        <stop offset="0" stop-color="#d2d3d4"/>
        <stop offset="0.45" stop-color="#8d8e90"/>
        <stop offset="0.72" stop-color="#4a4b4e"/>
        <stop offset="0.9" stop-color="#232325"/>
        <stop offset="1" stop-color="#111"/>
      </radialGradient>
      <radialGradient id="tyre-small" cx="0.5" cy="0.5" r="0.55">
        <stop offset="0" stop-color="#e4e4e5"/>
        <stop offset="0.55" stop-color="#aeafb1"/>
        <stop offset="0.72" stop-color="#3b3c3f"/>
        <stop offset="1" stop-color="#121213"/>
      </radialGradient>
    </defs>
    <g role="img" aria-label="Close-up photo of a large tyre">
      <circle cx="590" cy="727" r="458" fill="url(#tyre-large)"/>
    </g>
    <circle cx="228" cy="185" r="290" fill="var(--red)"/>
    <g role="img" aria-label="Close-up photo of a tyre framing the company name">
      <circle cx="205" cy="158" r="274" fill="url(#tyre-small)"/>
    </g>
  </svg>

  <div class="brand">
    <div class="name">TORNILEX</div>
    <div class="tag">AUTO TRANSPORT</div>
  </div>

  <h1 class="offer headline">WE PROVIDE<br>AUTO TOWING<br>FOR</h1>
  <div class="offer price">$75.00</div>
  <div class="offer price-label">Guarantee</div>

  <p class="offer promise p1">We Guarantee you will only pay <span class="hot">&nbsp;$75.00</span></p>
  <p class="offer promise p2">in the city of Houston</p>
  <p class="offer promise p3">We Guarantee to pick up your Auto in</p>
  <p class="offer promise p4"><span class="hot">24 hours</span> or less</p>

  <p class="offer closer">WE WANT TO EARN YOUR BUSINESS!</p>

  <div class="contact c-phone">
    <svg width="22" height="22" viewBox="0 0 24 24"><path fill="#fff" d="M6.6 10.8a15.1 15.1 0 0 0 6.6 6.6l2.2-2.2c.3-.3.7-.4 1-.2 1.1.4 2.3.6 3.6.6.6 0 1 .4 1 1V20c0 .6-.4 1-1 1A17 17 0 0 1 3 4c0-.6.4-1 1-1h3.5c.6 0 1 .4 1 1 0 1.3.2 2.5.6 3.6.1.3 0 .7-.2 1z"/></svg>
    <span>(281) 555-0137</span>
  </div>
  <div class="contact c-web">
    <svg width="20" height="16" viewBox="0 0 20 16"><rect x="1" y="1" width="18" height="14" fill="none" stroke="#fff" stroke-width="2"/><path d="M1 1l9 7 9-7" fill="none" stroke="#fff" stroke-width="2"/></svg>
    <span>www.tornilexautotransport.com</span>
  </div>
  <div class="contact c-mail">
    <svg width="20" height="20" viewBox="0 0 20 20"><circle cx="10" cy="10" r="8.5" fill="none" stroke="#fff" stroke-width="1.8"/><ellipse cx="10" cy="10" rx="3.8" ry="8.5" fill="none" stroke="#fff" stroke-width="1.5"/><path d="M1.5 10h17M3 5.5h14M3 14.5h14" stroke="#fff" stroke-width="1.5"/></svg>
    <span>service@tornilexautotransport.com</span>
  </div>
</main>
</body>
</html>
```